Corporate Identity Design Project

Marisol Tevendry Design is a small boutique event planning and floral design company, based in Northern Alberta. I require the creation of some corporate identity pieces. I want a minimalistic design.
Website www.marisoltevendry.com

Pieces should include
1. Business Card
Should include the company logo, name, email address, address, phone number. These will be professional printed.
These are three cards that I like:
http://cardlayoutgallerynook.com/wp-content/uploads/2010/02/Renata_Voskuilen_Roomworks_by_Pepperleaf_studio_Graphics.jpg
http://tidycardshowcase.com/wp-content/uploads/2011/06/Quietfold-Studio-Minimalist-Business-Cards_11.jpg
http://graphiclanternhub.com/wp-content/uploads/2012/03/16.minimalist-business-cards.jpg
I like letterpress, but I am open to other options.

2. Letterhead
will be professionally printed

3. Envelope

4. Fax Sheet
will be printed on home printer

5. Pocket Presentation
Like -http://fernwickgardenworks.com/img/design_step_proposal@2x.jpg

6. Invoice
Like - http://velmaquorlin.files.blogsite-example.com/2011/02/summit-strength-4-letterhead-combined.png?w=529

7. Proposal
Like something like this – this will not be printed, but rather emailed to clients
Like http://getfile7.brindlepost.com/getfile/files.brindlepost.com/tarnu-studio/qwRtZe8MmXp3LoKcV7B2nhdYJsaWeFUy6gT4rkPHvxiQbNcDzA9jsLE/Picture-52.png.scaled.500.jpg

8. Contract
Like http://www.brightkeelpromo.co.uk/images/tamsin-contract.jpg

9. Business Brochure – I have removed this piece from the project and will most likely post it as another project at a later date.

If you think that this is a project of interest to you, but feel that it is “too much” work for the price, please let me know how you would re-package it – I am open to suggestions.

Target Market(s)

Young women

Industry/Entity Type

Boutique

Requirements
Should not have
• I do not want it to look "frilly"

```html
<!DOCTYPE html>
<html lang="en">
<head>
<meta charset="utf-8">
<title>Marisol Tevendry Design – Business Cards</title>
<link href="https://fonts.googleapis.com/css2?family=Marcellus+SC&family=Montserrat:wght@700&family=Open+Sans:wght@400&display=swap" rel="stylesheet">
<style>
  :root {
    --page-bg: #ecebe9;
    --card-light: #ffffff;
    --card-shade: #e4e4e4;
    --ink: #1c1c1c;
    --ink-soft: #4a4a4a;
    --mark-grey: #b9b9b9;
    --brand-pink: #e27a80;
    --silver-hi: #f7f7f7;
    --silver-lo: #b8b8b8;
  }
  * { box-sizing: border-box; margin: 0; padding: 0; }
  html, body { width: 1200px; height: 900px; overflow: hidden; }
  body { background: var(--page-bg); position: relative; }

  .card {
    position: absolute;
    width: 620px;
    height: 354px;
    background: linear-gradient(160deg, var(--card-light) 0%, var(--card-shade) 100%);
    box-shadow: 0 6px 18px rgba(0,0,0,0.18);
    overflow: hidden;
  }

  /* Contact side */
  .card--contact { left: 60px; top: 90px; }
  .card--contact .holder-name {
    position: absolute;
    right: 64px;
    top: 56px;
    font-family: "Marcellus SC", serif;
    font-size: 30px;
    letter-spacing: 1px;
    color: var(--ink-soft);
  }
  .card--contact .details {
    position: absolute;
    right: 40px;
    top: 122px;
    text-align: right;
    font-family: "Open Sans", sans-serif;
    font-size: 14px;
    line-height: 21px;
    color: var(--ink-soft);
    font-style: normal;
  }
  .card--contact .brand-disc {
    position: absolute;
    left: -40px;
    top: 90px;
    width: 230px;
    height: 230px;
    border-radius: 50%;
    background: var(--mark-grey);
    opacity: 0.45;
  }
  .card--contact .brand-name {
    position: absolute;
    left: 36px;
    bottom: 40px;
    font-family: "Montserrat", sans-serif;
    font-weight: 700;
    font-size: 30px;
    line-height: 32px;
    letter-spacing: 4px;
    text-transform: uppercase;
    color: var(--brand-pink);
  }

  /* Logo side */
  .card--logo { left: 520px; top: 470px; }
  .card--logo .frame {
    position: absolute;
    inset: 22px;
    border: 6px solid var(--silver-lo);
    border-image: linear-gradient(135deg, var(--silver-hi), var(--silver-lo), var(--silver-hi), var(--silver-lo)) 1;
  }
  .card--logo .lockup {
    position: absolute;
    left: 0; right: 0; top: 0; bottom: 0;
    display: flex;
    align-items: center;
    justify-content: center;
    gap: 22px;
  }
  .card--logo .brand-disc {
    width: 78px;
    height: 78px;
    border-radius: 50%;
    background: var(--mark-grey);
  }
  .card--logo .brand-name {
    font-family: "Montserrat", sans-serif;
    font-weight: 700;
    font-size: 26px;
    line-height: 30px;
    letter-spacing: 4px;
    text-transform: uppercase;
    color: var(--ink);
  }
</style>
</head>
<body>

  <section class="card card--contact" aria-label="Business card, contact side">
    <div class="brand-disc" aria-hidden="true"></div>
    <h1 class="holder-name">Marisol Tevendry</h1>
    <address class="details">
      Phone: (111)111-1111<br>
      Adress Line 1<br>
      Adress Line 2<br>
      www.marisoltevendry.com<br>
      Email: contact@marisoltevendry.com
    </address>
    <p class="brand-name">Marisol<br>Tevendry<br>Design</p>
  </section>

  <section class="card card--logo" aria-label="Business card, logo side">
    <div class="frame" aria-hidden="true"></div>
    <div class="lockup">
      <div class="brand-disc" aria-hidden="true"></div>
      <p class="brand-name">Marisol<br>Tevendry<br>Design</p>
    </div>
  </section>

</body>
</html>
```